Baby Care Print Log for Nannies and Parents- Creating a brand/style I can use across different forms

I am creating a notebook for babysitters to use to communicate with parents about the children they care for. I will be creating many different forms (emergency contacts, daily logs, shopping lists, etc.)
I need a look and feel from which to style these forms from. I am starting by designing the daily baby care log. I need a designer to take my Word doc with just text on it, and create a visual approach to make this visually appealing.
I do not want this to be extremely "babyish" with cartoon styling. I want it to be more of a professional looking style. I would like to be able to color each different document a different color palette, yet keep the similar look and feel. My logo is attached for inspiration. I use real photography across my website velmorapath.com.
Updates
I will be re-designing my Wordpress website based on what design I like best and also will need other forms completed once I pick a design. I am hoping to work with someone who I can hire for further development needs as well. Added Saturday, February 11, 2017
Target Market(s)
Professional Parents
Industry/Entity Type
Education
Requirements
Must have
- color, pop, visual appeal
- Please use the color in my logo and any complementary colors that you think work well with it. I definitely like colored patterns, ombre, colored backgrounds, etc. I'd prefer for it not to be completely white with only pops of color here and there.
Nice to have
- My logo somewhere subtly on the form
- Photography elements
Should not have
- cartoon images of babies, etc. I use real photography across my website with the exception of my logo umbrella.

```html
<!DOCTYPE html>
<html lang="en">
<head>
<meta charset="utf-8">
<title>Velmora Notes – Daily Baby Care Log</title>
<link rel="stylesheet" href="https://fonts.googleapis.com/css2?family=Lato:wght@400;700&display=swap">
<style>
  :root {
    --page-yellow: #fef59c;
    --band-yellow: #fff7b4;
    --panel-cream: #fffbd8;
    --sky-blue: #5bc3df;
    --ink: #3a3a3a;
    --rule: #9c9c94;
    --shadow: #bdbdbd;
    --white: #ffffff;
  }
  * { box-sizing: border-box; margin: 0; padding: 0; }
  html, body { width: 1200px; height: 1000px; overflow: hidden; background: var(--white); }
  body { font-family: "Lato", Arial, sans-serif; color: var(--ink); position: relative; }

  .sheet-shadow { position: absolute; left: 265px; top: 35px; width: 653px; height: 927px; background: var(--shadow); }
  .sheet { position: absolute; left: 253px; top: 25px; width: 657px; height: 927px; background: var(--white); }
  .sheet-body { position: absolute; left: 0; top: 150px; width: 657px; height: 777px; background: var(--page-yellow); }
  .feeding-band { position: absolute; left: 0; top: 355px; width: 657px; height: 147px; background: var(--band-yellow); }

  .brand { position: absolute; left: 44px; top: 27px; display: flex; align-items: center; gap: 8px; font-size: 19px; font-weight: 700; color: var(--ink); }
  .brand-dot { width: 14px; height: 14px; border-radius: 50%; background: var(--sky-blue); }

  .field-name { position: absolute; left: 0; top: 63px; width: 283px; height: 54px; background: var(--page-yellow); font-size: 13px; padding: 23px 0 0 41px; }
  .field-date { position: absolute; left: 0; top: 117px; width: 283px; height: 33px; background: var(--sky-blue); color: var(--white); font-size: 13px; padding: 8px 0 0 41px; }

  .photo { position: absolute; }
  .photo-bath { left: 287px; top: 5px; width: 140px; height: 145px; background: radial-gradient(ellipse at 50% 55%, #f2d4bd 0%, #f4ece6 45%, #ffffff 80%); }
  .photo-sleep { left: 432px; top: 0; width: 225px; height: 150px; background: linear-gradient(135deg, #e6e6e4 0%, #f4f3f1 40%, #e9d6cf 65%, #dcdcda 100%); }

  .tag { position: absolute; height: 25px; background: var(--sky-blue); color: var(--white); font-size: 15px; font-weight: 700; letter-spacing: 0.3px; border-radius: 4px; padding: 3px 0 0 9px; }
  .label { position: absolute; font-size: 11px; letter-spacing: 0.6px; text-transform: uppercase; }
  .mood { position: absolute; font-size: 16px; letter-spacing: 1px; }
  .supply { position: absolute; font-size: 13px; font-weight: 700; }

  .activities-panel { position: absolute; left: 262px; top: 524px; width: 358px; height: 150px; background: var(--panel-cream); border-radius: 8px; }

  .rules { position: absolute; left: 0; top: 0; }
</style>
</head>
<body>
  <div class="sheet-shadow"></div>
  <main class="sheet">
    <div class="sheet-body"></div>
    <div class="feeding-band"></div>

    <div class="brand"><span class="brand-dot"></span>Velmora Notes</div>

    <div class="field-name">Name</div>
    <div class="field-date">Date</div>

    <div class="photo photo-bath" role="img" aria-label="Photo of a baby sitting in a small white bath tub"></div>
    <div class="photo photo-sleep" role="img" aria-label="Photo of a newborn yawning on white blankets"></div>

    <div class="activities-panel"></div>

    <!-- Nap time -->
    <div class="tag" style="left:32px;top:188px;width:93px;">NAP TIME</div>
    <div class="label" style="left:41px;top:221px;">Time</div>
    <div class="label" style="left:105px;top:221px;">How long</div>

    <!-- Mood -->
    <div class="tag" style="left:286px;top:188px;width:93px;">MOOD</div>
    <div class="mood" style="left:295px;top:231px;">HAPPY</div>
    <div class="mood" style="left:425px;top:231px;">SAD</div>
    <div class="mood" style="left:523px;top:231px;">UNSETTLED</div>
    <div class="mood" style="left:295px;top:269px;">ENERGETIC</div>
    <div class="mood" style="left:425px;top:269px;">TIRED</div>
    <div class="mood" style="left:295px;top:307px;">CHATTY</div>
    <div class="mood" style="left:425px;top:307px;">QUIET</div>

    <!-- Feeding -->
    <div class="tag" style="left:32px;top:344px;width:94px;">FEEDING</div>
    <div class="label" style="left:44px;top:377px;">Time</div>
    <div class="label" style="left:108px;top:377px;">Milk (type)</div>
    <div class="label" style="left:242px;top:377px;">Water</div>
    <div class="label" style="left:376px;top:377px;">Food</div>
    <div class="label" style="left:507px;top:377px;">Amount</div>

    <!-- Diapers -->
    <div class="tag" style="left:32px;top:514px;width:94px;">DIAPERS</div>
    <div class="label" style="left:44px;top:552px;">Time</div>
    <div class="label" style="left:152px;top:552px;">Wet</div>
    <div class="label" style="left:194px;top:552px;">BM</div>

    <div class="tag" style="left:286px;top:514px;width:172px;">TODAY'S ACTIVITIES</div>

    <!-- Supplies -->
    <div class="tag" style="left:32px;top:691px;width:207px;">SUPPLIES NEEDED SOON</div>
    <div class="supply" style="left:69px;top:731px;">DIAPERS</div>
    <div class="supply" style="left:214px;top:731px;">MILK / FORMULA</div>
    <div class="supply" style="left:368px;top:731px;">WET WIPES</div>
    <div class="supply" style="left:503px;top:731px;">OTHERS:</div>
    <div class="supply" style="left:69px;top:760px;">DIAPER CREAM</div>
    <div class="supply" style="left:214px;top:760px;">CEREAL</div>
    <div class="supply" style="left:368px;top:760px;">BABY'S FOOD</div>

    <!-- Special notes -->
    <div class="tag" style="left:32px;top:798px;width:144px;">SPECIAL NOTES</div>

    <svg class="rules" width="657" height="927" viewBox="0 0 657 927" aria-hidden="true">
      <g stroke="var(--rule)" stroke-width="1" fill="none">
        <!-- nap -->
        <path d="M39 256H92M105 256H218M39 276H92M105 276H218M39 296H92M105 296H218M39 316H92M105 316H218"/>
        <!-- feeding -->
        <path d="M42 412H96M108 412H231M242 412H365M376 412H498M507 412H630
                 M42 432H96M108 432H231M242 432H365M376 432H498M507 432H630
                 M42 452H96M108 452H231M242 452H365M376 452H498M507 452H630
                 M42 472H96M108 472H231M242 472H365M376 472H498M507 472H630"/>
        <!-- diapers -->
        <path d="M41 587H132M41 607H132M41 627H132M41 647H132M41 669H132"/>
        <!-- others & notes -->
        <path d="M504 774H619M42 844H619M42 864H619M42 884H619"/>
      </g>
      <g stroke="#777" stroke-width="1" fill="var(--white)">
        <rect x="155.5" y="571.5" width="18" height="16"/><rect x="195.5" y="571.5" width="18" height="16"/>
        <rect x="155.5" y="593.5" width="18" height="16"/><rect x="195.5" y="593.5" width="18" height="16"/>
        <rect x="155.5" y="615.5" width="18" height="16"/><rect x="195.5" y="615.5" width="18" height="16"/>
        <rect x="155.5" y="637.5" width="18" height="16"/><rect x="195.5" y="637.5" width="18" height="16"/>
        <rect x="155.5" y="658.5" width="18" height="16"/><rect x="195.5" y="658.5" width="18" height="16"/>
        <circle cx="50" cy="739" r="11.5"/><circle cx="196" cy="739" r="11.5"/>
        <circle cx="350" cy="739" r="11.5"/><circle cx="485" cy="739" r="11.5"/>
        <circle cx="50" cy="768" r="11.5"/><circle cx="196" cy="768" r="11.5"/>
        <circle cx="350" cy="768" r="11.5"/>
      </g>
    </svg>
  </main>
</body>
</html>
```